Wendale Information Posters for Student signage

Secondary school looking for some posters to display throughout the school with fresh designs using school colours and fitting with general feel of the school's graphic image. The final designs should be welcoming but clearly outline the required instructions. Sample designs that have been created by the school are attached with the relevant information that is required to appear on the signs. School would like a more dynamic design than the basic signs attached.
We are looking for:
- Large pop-up banner style size for the 2 posters called
"Ready for class" and "Morning Routine".
- Printable poster for the "Wendale Outdoor" sign.

Please incorporate a design feature of "the Wendale 1,2,3" into the posters and also use the Wendale Leaner values of Integrity, Compassion, Curiosity and Drive to help illustrate the content.

An option for design is to incorporate our school's first nations artwork into the design and i have also provided various extracts of design pieces that the school often uses in it's marketing materials.

Target Market(s)

Secondary School Students

Industry/Entity Type

Education

Colors
00AB8E
00BBA5
67D7C9
C6EFE9
E9F9F6
FFF300
FFF600
FEFA6F
FFFEC7
FFFEE8
FFC000
F8CF3A
FAE287
FDF2CF
FEFAEE

Requirements
Must have
• My project must have eyecatching graphics

```html
<!DOCTYPE html>
<html lang="en">
<head>
<meta charset="utf-8">
<title>Wendale Student Signage</title>
<link href="https://fonts.googleapis.com/css2?family=Poppins:wght@500;600;700;800;900&family=Libre+Baskerville:ital,wght@1,700&display=swap" rel="stylesheet">
<style>
:root{
  --green:#1f3b17;
  --green-soft:#2b4a22;
  --yellow:#f6e531;
  --yellow-line:#f4e23a;
  --white:#ffffff;
  --rule:#cfcfcf;
  --page:#ecebe7;
}
*{box-sizing:border-box;margin:0;padding:0}
html,body{width:1200px;height:800px;overflow:hidden}
body{background:var(--page);font-family:'Poppins',sans-serif;color:var(--green);position:relative}
.sign{position:absolute;background:var(--white);overflow:hidden;box-shadow:0 2px 10px rgba(0,0,0,.12)}
.banner{width:240px;height:600px;top:100px}
.banner--ready{left:190px}
.banner--routine{left:455px}
.poster{left:735px;top:140px;width:245px;height:325px}
.wave-top{position:absolute;left:0;top:0;width:100%}
.wave-bottom{position:absolute;left:0;bottom:0;width:100%}
.footer{position:absolute;right:12px;bottom:22px;display:flex;align-items:center;gap:8px}
.footer__values{text-align:right;line-height:1.15}
.footer__value{color:var(--white);font-weight:800;font-size:10px}
.footer__label{color:var(--yellow);font-weight:500;font-size:7.5px}
.school-mark{display:flex;align-items:center;gap:4px;color:var(--yellow);font-weight:800;font-size:11px}
.school-mark__dot{width:10px;height:10px;border-radius:50%;background:var(--yellow)}
.heading{position:absolute;left:0;right:0;text-align:center;font-weight:800}
.frame{position:absolute;border:3px solid var(--yellow-line);border-radius:10px;background:var(--white)}
.tab{position:absolute;left:50%;transform:translateX(-50%);background:var(--yellow);border-radius:8px;font-weight:700;text-align:center;white-space:nowrap}
.tab__inner{background:var(--white);border-radius:5px;margin:3px;padding:2px 8px}
.nums{display:flex;justify-content:center;gap:6px}
.num{display:inline-flex;align-items:center;justify-content:center;border-radius:50%;background:var(--green);color:var(--white);font-weight:800}
.icon{flex:none;border-radius:50%;background:var(--yellow);display:flex;align-items:center;justify-content:center}

/* Ready for class */
.ready__title{top:66px;font-size:23px;line-height:1.2}
.ready__frame{left:13px;right:13px;top:175px;height:290px}
.ready__tab{top:-18px;padding:0 0 4px}
.ready__tab .tab__inner{font-size:17px;padding:1px 12px}
.ready__tab .num{width:19px;height:19px;font-size:11px}
.ready__tab .nums{gap:22px;margin-top:3px}
.ready__list{position:absolute;left:0;right:0;top:44px}
.ready__item{display:flex;align-items:center;gap:10px;padding:0 14px 0 16px;height:80px;border-bottom:1px dotted var(--rule)}
.ready__item:last-child{border-bottom:none}
.ready__item .icon{width:60px;height:60px}
.ready__text{font-weight:700;font-size:16px;line-height:1.02}
.ready__text small{display:block;font-size:12px;font-weight:600}

/* Morning routine */
.routine__title{top:50px;font-size:31px;line-height:.92;font-weight:900}
.routine__tab{top:122px;left:50%;transform:translateX(-50%);display:flex;align-items:center;gap:6px;padding:3px 4px 3px 8px;font-size:16px;font-weight:700}
.routine__tab .nums{background:var(--white);border-radius:5px;padding:2px 4px;gap:4px}
.routine__tab .num{width:17px;height:17px;font-size:10px}
.routine__motto{position:absolute;top:160px;left:0;right:0;text-align:center;font-family:'Libre Baskerville',serif;font-style:italic;font-weight:700;font-size:10.5px}
.step-box{left:14px;right:14px}
.step-box--ontime{top:190px;height:140px}
.step-box--late{top:346px;height:140px}
.step-box__tab{top:-11px;font-size:12px;font-weight:800;padding:1px 8px}
.steps{position:absolute;left:10px;right:10px;top:12px}
.step{display:flex;align-items:center;gap:8px;height:40px;border-bottom:1px dotted var(--rule)}
.step:last-child{border-bottom:none}
.step .num{width:22px;height:22px;font-size:12px;flex:none}
.step .icon{width:24px;height:24px}
.step__text{font-size:8px;font-weight:700;line-height:1.15;margin-left:10px}

/* Outdoor poster */
.outdoor__title{top:48px;font-size:12.5px;line-height:1.2}
.outdoor__frame{left:14px;right:14px;top:106px;height:140px}
.outdoor__tab{top:-20px;font-size:10px;padding:0 0 3px}
.outdoor__tab .tab__inner{padding:0 8px}
.outdoor__tab .num{width:12px;height:12px;font-size:7px}
.outdoor__tab .nums{gap:14px;margin-top:2px}
.outdoor__list{position:absolute;left:8px;right:8px;top:16px}
.outdoor__item{display:flex;align-items:center;gap:10px;height:38px;border-bottom:1px dotted var(--rule);font-size:20px;font-weight:800}
.outdoor__item:last-child{border-bottom:none}
.outdoor__item .icon{width:30px;height:30px}
.poster .footer{bottom:12px;right:10px}
</style>
</head>
<body>

<!-- Ready for class banner -->
<section class="sign banner banner--ready" aria-label="Are you ready for class banner">
  <svg class="wave-top" viewBox="0 0 240 55" height="55" role="img" aria-label="First Nations artwork band in yellow">
    <path d="M0 0H240V18C190 22 150 48 90 50C50 52 20 44 0 40Z" fill="#f6e531"/>
  </svg>
  <h1 class="heading ready__title">Are you ready<br>for class?</h1>
  <div class="frame ready__frame">
    <div class="tab ready__tab">
      <div class="tab__inner">The Wendale</div>
      <div class="nums"><span class="num">1</span><span class="num">2</span><span class="num">3</span></div>
    </div>
    <ul class="ready__list" style="list-style:none">
      <li class="ready__item">
        <span class="icon"><svg width="34" height="26" viewBox="0 0 34 26"><rect x="5" y="2" width="24" height="17" rx="1.5" fill="#1f3b17"/><rect x="1" y="20" width="32" height="4" rx="1.5" fill="#1f3b17"/></svg></span>
        <span class="ready__text">Laptop /<br>workbook</span>
      </li>
      <li class="ready__item">
        <span class="icon"><svg width="22" height="36" viewBox="0 0 22 36"><rect x="3" y="2" width="16" height="32" rx="5" fill="none" stroke="#1f3b17" stroke-width="2.5"/><circle cx="11" cy="8" r="2.2" fill="#1f3b17"/></svg></span>
        <span class="ready__text">Phone in<br>Lockpod</span>
      </li>
      <li class="ready__item">
        <span class="icon"><svg width="40" height="24" viewBox="0 0 40 24"><path d="M12 3H28L30 15H10Z" fill="#1f3b17"/><ellipse cx="20" cy="17" rx="18" ry="4" fill="#1f3b17"/></svg></span>
        <span class="ready__text">Correct<br>uniform<small>(including hat)</small></span>
      </li>
    </ul>
  </div>
  <svg class="wave-bottom" viewBox="0 0 240 130" height="130" role="img" aria-label="First Nations artwork band in green">
    <path d="M0 50C50 20 90 70 150 40C190 20 220 10 240 5V130H0Z" fill="#1f3b17"/>
  </svg>
  <div class="footer">
    <div class="footer__values"><div class="footer__value">Curiosity and Drive</div><div class="footer__label">Wendale Leaner Values</div></div>
    <div class="school-mark"><span class="school-mark__dot"></span>Wendale</div>
  </div>
</section>

<!-- Morning routine banner -->
<section class="sign banner banner--routine" aria-label="Morning routine banner">
  <svg class="wave-top" viewBox="0 0 240 55" height="55" role="img" aria-label="First Nations artwork band in yellow">
    <path d="M0 0H240V12C200 14 160 36 100 40C60 44 25 46 0 48Z" fill="#f6e531"/>
  </svg>
  <h1 class="heading routine__title">MORNING<br>ROUTINE</h1>
  <div class="tab routine__tab">The Wendale <span class="nums"><span class="num">1</span><span class="num">2</span><span class="num">3</span></span></div>
  <p class="routine__motto">Early is on time, on time is late!</p>

  <div class="frame step-box step-box--ontime">
    <div class="tab step-box__tab">ON TIME</div>
    <ul class="steps" style="list-style:none">
      <li class="step"><span class="num">1</span><span class="icon"><svg width="16" height="16" viewBox="0 0 16 16"><circle cx="8" cy="8" r="6.5" fill="none" stroke="#1f3b17" stroke-width="1.5"/><path d="M8 4V8L11 10" stroke="#1f3b17" stroke-width="1.5" fill="none"/></svg></span><span class="step__text">Arrive before<br>8:30 AM</span></li>
      <li class="step"><span class="num">2</span><span class="icon" role="img" aria-label="Locker icon"><svg width="14" height="14" viewBox="0 0 14 14"><rect x="1" y="1" width="5" height="12" fill="#1f3b17"/><rect x="8" y="1" width="5" height="12" fill="#1f3b17"/></svg></span><span class="step__text">Place Bag in<br>Locker</span></li>
      <li class="step"><span class="num">3</span><span class="icon" role="img" aria-label="Assembly icon"></span><span class="step__text">Arrive at Home Group /<br>House Assembly<br>before 8:40 AM</span></li>
    </ul>
  </div>

  <div class="frame step-box step-box--late">
    <div class="tab step-box__tab">RUNNING LATE</div>
    <ul class="steps" style="list-style:none">
      <li class="step"><span class="num">1</span><span class="icon" role="img" aria-label="Student Services building icon"></span><span class="step__text">Sign in at<br>Student Services</span></li>
      <li class="step"><span class="num">2</span><span class="icon" role="img" aria-label="Locker icon"><svg width="14" height="14" viewBox="0 0 14 14"><rect x="1" y="1" width="5" height="12" fill="#1f3b17"/><rect x="8" y="1" width="5" height="12" fill="#1f3b17"/></svg></span><span class="step__text">Place bag in Locker</span></li>
      <li class="step"><span class="num">3</span><span class="icon" role="img" aria-label="Classroom icon"></span><span class="step__text">Prompt arrival to<br>class expected</span></li>
    </ul>
  </div>

  <svg class="wave-bottom" viewBox="0 0 240 110" height="110" role="img" aria-label="First Nations artwork band in green">
    <path d="M0 40C40 10 90 50 150 30C190 18 220 8 240 4V110H0Z" fill="#1f3b17"/>
  </svg>
  <div class="footer">
    <div class="footer__values"><div class="footer__value">Integrity</div><div class="footer__label">Wendale Leaner Values</div></div>
    <div class="school-mark"><span class="school-mark__dot"></span>Wendale</div>
  </div>
</section>

<!-- Outdoor hats poster -->
<section class="sign poster" aria-label="Wendale Outdoor hats poster">
  <svg class="wave-top" viewBox="0 0 245 40" height="40" role="img" aria-label="First Nations artwork band in yellow">
    <path d="M0 0H245V8C200 10 160 24 100 30C60 34 25 36 0 38Z" fill="#f6e531"/>
  </svg>
  <h1 class="heading outdoor__title">We wear HATS at Wendale<br>when outdoors...</h1>
  <div class="frame outdoor__frame">
    <div class="tab outdoor__tab">
      <div class="tab__inner">The Wendale</div>
      <div class="nums"><span class="num">1</span><span class="num">2</span><span class="num">3</span></div>
    </div>
    <ul class="outdoor__list" style="list-style:none">
      <li class="outdoor__item"><span class="icon" role="img" aria-label="Figure walking with hat"></span>WALKING</li>
      <li class="outdoor__item"><span class="icon" role="img" aria-label="Figure sitting with hat"></span>SITTING</li>
      <li class="outdoor__item"><span class="icon" role="img" aria-label="Figure playing ball with hat"></span>PLAYING</li>
    </ul>
  </div>
  <svg class="wave-bottom" viewBox="0 0 245 80" height="80" role="img" aria-label="First Nations artwork band in green">
    <path d="M0 30C50 10 100 40 160 22C200 10 225 4 245 0V80H0Z" fill="#1f3b17"/>
  </svg>
  <div class="footer">
    <div class="footer__values"><div class="footer__value">Integrity</div><div class="footer__label">Wendale Leaner Values</div></div>
    <div class="school-mark"><span class="school-mark__dot"></span>Wendale</div>
  </div>
</section>

</body>
</html>
```